Spice Mix Label Bottle Branding - Health and Weight Loss Mixes

The company is called ZestoLane Spice Mix's. We've created 5 spice mixes using ingredients that promote health and weight loss. We already have a logo but now we need labels for our bottles. We would like to see designs that have the feel of health supplements (see attached examples)

We would like a different colour featured with each of our flavours.

Our flavours are:
-Golden Chai (Yellow)
-Mild Curry (Orange)
-Coffee Rub (brown)
-Garlic Oregano (Green)
-Taco (Blue)

Thank you!

Target Market(s)

Ages 22-35. Men and Female. Trendy, Hipster.

Industry/Entity Type

Food Production

Font styles to use
Sans Serif

Colors
f37122
0655a3
0692cd
9bcb3c
fbee3f

Requirements
Must have
• A different featured colour for each flavour.
• The ZestoLane Spices Logo (attached)
• The slogan: "Weight Loss Ingredients"
• -Golden Chai (Yellow)
• -Mild Curry (Orange)
• -Coffee Rub (brown)
• -Garlic Oregano (Green)
• -Taco (Blue)
• Text Files attached.
Nice to have
• A black label with a featured colour for each of the spice mice flavours.
• 'No Salt added'

```html
<!DOCTYPE html>
<html lang="en">
<head>
<meta charset="utf-8">
<title>ZestoLane Spices – Mild Curry Label</title>
<link rel="stylesheet" href="https://fonts.googleapis.com/css2?family=Oswald:wght@700&family=Montserrat:wght@700&family=Roboto+Condensed:wght@700&display=swap">
<style>
  :root {
    --page: #ffffff;
    --label-black: #0d0d0d;
    --flavour-orange: #f37122;
    --flavour-orange-deep: #c2440f;
    --label-white: #ffffff;
  }
  * { margin: 0; padding: 0; box-sizing: border-box; }
  html, body {
    width: 1112px;
    height: 1200px;
    overflow: hidden;
    background: var(--page);
  }
  .canvas {
    position: relative;
    width: 1112px;
    height: 1200px;
  }
  .label {
    position: absolute;
    left: 106px;
    top: 240px;
    width: 900px;
    height: 720px;
    background: var(--label-black);
    overflow: hidden;
  }
  .label__side-bands {
    position: absolute;
    inset: 0;
    width: 900px;
    height: 720px;
  }
  .label__content {
    position: absolute;
    inset: 0;
    display: flex;
    flex-direction: column;
    align-items: center;
  }
  .brand-name {
    margin-top: 150px;
    font-family: "Oswald", "Arial Narrow", sans-serif;
    font-weight: 700;
    font-size: 84px;
    line-height: 1;
    color: var(--label-white);
    letter-spacing: 1px;
  }
  .tagline {
    margin-top: 26px;
    padding-bottom: 10px;
    border-bottom: 3px solid var(--label-white);
    font-family: "Montserrat", Arial, sans-serif;
    font-weight: 700;
    font-size: 28px;
    letter-spacing: 0.5px;
    color: var(--label-white);
  }
  .flavour-ribbon {
    position: relative;
    margin-top: 62px;
    width: 580px;
    height: 88px;
  }
  .flavour-ribbon__shape {
    position: absolute;
    inset: 0;
    width: 580px;
    height: 88px;
  }
  .flavour-ribbon__name {
    position: relative;
    display: block;
    text-align: center;
    line-height: 88px;
    font-family: "Roboto Condensed", "Arial Narrow", sans-serif;
    font-weight: 700;
    font-size: 58px;
    letter-spacing: 2px;
    color: var(--label-white);
  }
  .net-weight {
    margin-top: 40px;
    font-family: "Roboto Condensed", "Arial Narrow", sans-serif;
    font-weight: 700;
    font-size: 30px;
    color: var(--label-white);
  }
</style>
</head>
<body>
  <main class="canvas">
    <section class="label" aria-label="Mild Curry spice label">
      <svg class="label__side-bands" viewBox="0 0 900 720" aria-hidden="true">
        <path d="M0 0 H70 Q150 360 70 720 H0 Z" fill="var(--flavour-orange-deep)"/>
        <path d="M900 0 H830 Q750 360 830 720 H900 Z" fill="var(--flavour-orange-deep)"/>
      </svg>
      <div class="label__content">
        <h1 class="brand-name">ZestoLane Spices</h1>
        <p class="tagline">WEIGHT LOSS SEASONINGS</p>
        <div class="flavour-ribbon">
          <svg class="flavour-ribbon__shape" viewBox="0 0 580 88" aria-hidden="true">
            <path d="M0 0 H580 L560 44 L580 88 H0 L20 44 Z" fill="var(--flavour-orange)"/>
          </svg>
          <span class="flavour-ribbon__name">MILD CURRY</span>
        </div>
        <p class="net-weight">Weight XXXg</p>
      </div>
    </section>
  </main>
</body>
</html>
```